Health Wellbeing Beauty online Shop

I have attached a full spec, however in summary this is a new business startup selling skincare products.

We need a web design for new wellbeing website, selling skincare products so need an eCommerce solution . On the home page I would like these faces to dissolve into each other on a loop or use a honeycomb style transation.
You will need the option of being able to log into an account, either through chatterbook, quorvix, tweedle or create an account. For created accounts, obviously need the facility to be able to reset passwords, see previous orders, track current order, and maintain favourites.
It should be PC, mobile and tablet friendly.

Look and Feel
It should be an elegant, modern, professional, trendy, unisex website. It should look clean and calm. Am happy to try interesting and slightly unusual designs. I would also like to have chat functionality, either powered by morvaLKtalk or by Quo 81.
Websites I like are
https://www.noble-radiance.example.co.uk/
https://www.onlyminerals.example.co.uk/
http://www.claramedica.example.com/

PLEASE DO USE YOUR KNOWELDGE OF WHAT WORKS FOR WEB DESIGN. YOU’RE THE EXPERT AND NEED YOUR EXPERTISE. CARTE BLANCHE TO DESIGN AS YOU SEE FIT. Please be creative, I need my site to stand out from the crowd.

Target Market(s)

Target Market
Middle aged women are our most common client, however, younger patients, both male and female, will often visit the site. In summary, I would like the site to appeal to all age brackets.

Requirements
Must have
• Need shop to be exactly like shop on this link http://www.claramedica.example.com/
Nice to have
• i would like something unique and creative

```html
<!DOCTYPE html>
<html lang="en">
<head>
<meta charset="utf-8">
<title>Lumen Vale Wellness – Skincare Shop</title>
<link rel="stylesheet" href="https://fonts.googleapis.com/css2?family=PT+Serif:ital,wght@0,400;0,700;1,400&family=Open+Sans:ital,wght@0,400;0,600;0,700;1,400&display=swap">
<style>
:root{
  --gold:#a8803f;
  --gold-dark:#8e6a30;
  --gold-light:#c49a55;
  --ink:#333333;
  --muted:#666666;
  --line:#d6d6d6;
  --dark:#222222;
  --darker:#1b1b1b;
  --star:#c8671c;
  --white:#ffffff;
}
*{box-sizing:border-box;margin:0;padding:0}
html,body{width:1200px;height:3393px;overflow:hidden;background:var(--white)}
body{position:relative;font-family:"Open Sans",Arial,sans-serif;color:var(--ink)}
.abs{position:absolute}
.serif{font-family:"PT Serif",Georgia,serif}

/* top bar */
.topbar{left:0;top:0;width:1200px;height:27px;background:var(--dark)}
.topbar .social{position:absolute;left:100px;top:9px;display:flex;gap:6px}
.topbar .social span{width:9px;height:9px;border-radius:50%;background:#cfcfcf}
.topbar .account{position:absolute;right:95px;top:5px;color:var(--white);font-size:13px;display:flex;gap:14px}

/* header */
.phone{left:107px;top:66px;font-size:12px;color:var(--ink)}
.brand{left:450px;top:10px;width:300px;text-align:center}
.brand-mark{width:78px;height:78px;border-radius:50%;border:2px solid #444;margin:0 auto}
.brand-name{font-family:"PT Serif",Georgia,serif;font-size:12.5px;letter-spacing:1px;color:#333;margin-top:10px}
.side-tab{left:1052px;top:27px;width:55px;height:132px;background:linear-gradient(90deg,#c9c9c9,#b7a07a);border-radius:0 0 6px 6px}
.side-tab .ic{position:absolute;left:15px;width:26px;height:26px;border-radius:50%;background:#2a2a2a;display:flex;align-items:center;justify-content:center}
.nav{left:95px;top:143px;width:1010px;display:flex;justify-content:center;gap:26px;font-size:12.5px;letter-spacing:.3px;color:var(--ink)}
.nav .caret{font-size:9px}
.nav-rule{left:95px;top:166px;width:955px;height:1px;background:var(--line)}
.dropdown{left:536px;top:173px;width:191px;background:var(--white);box-shadow:0 2px 8px rgba(0,0,0,.25);z-index:5}
.dropdown li{list-style:none;height:42px;line-height:42px;padding-left:10px;font-size:12px;color:#555;border-bottom:1px solid #e6e6e6}

/* hero */
.hero{left:95px;top:177px;width:1010px;height:419px;overflow:hidden;
  background:radial-gradient(ellipse at 78% 55%,#f4ede4 0%,#d9c6ad 38%,rgba(0,0,0,0) 70%),linear-gradient(90deg,#5b4637 0%,#8b725a 30%,#b99c7e 55%,#cbb498 100%)}
.hero-shade{left:0;top:0;width:420px;height:419px;background:linear-gradient(90deg,rgba(35,27,22,.72),rgba(35,27,22,.35) 85%,rgba(0,0,0,0))}
.hero-products{left:655px;top:39px;width:340px;height:305px;border-radius:10px;background:radial-gradient(ellipse at center,#f7f2e8 0%,#e9dcc3 55%,rgba(233,220,195,0) 100%)}
.hero-copy{left:25px;top:106px;width:335px;color:var(--white)}
.hero-copy .hello{font-size:17px;font-weight:700}
.hero-copy .title{font-size:20px;letter-spacing:.5px;margin-top:2px}
.hero-copy p{font-size:11.5px;line-height:15px;margin-top:10px}
.btn-offer{left:25px;top:269px;width:148px;height:30px;border:1.5px solid var(--white);border-radius:4px;color:var(--white);font-size:14px;text-align:center;line-height:27px}
.badge-off{left:235px;top:261px;width:86px;height:74px;border-radius:50%;background:var(--white);color:var(--gold);text-align:center;padding-top:18px}
.badge-off b{font-family:"PT Serif",Georgia,serif;font-size:28px;font-weight:400}
.badge-off small{font-size:10px;vertical-align:top}
.dots{left:483px;top:399px;display:flex;gap:5px}
.dots span{width:8px;height:8px;border-radius:50%;background:#eee;opacity:.8}
.dots span:first-child{background:var(--white);opacity:1}

/* shop */
.section-title{left:0;width:1200px;text-align:center;font-family:"PT Serif",Georgia,serif;color:#444}
.shop-title{top:628px;font-size:29px;letter-spacing:1px}
.shop-rule{left:507px;top:678px;width:186px;height:1px;background:#bfbfbf}
.filters{left:0;top:718px;width:1200px;display:flex;justify-content:center;gap:14px;font-size:13px;color:#444}
.filters span{padding:3px 6px}
.filters .on{background:var(--gold);color:var(--white)}

.card{width:212px;height:375px;border:1px solid #dedede;background:var(--white)}
.card .thumb{position:absolute;left:10px;top:10px;width:190px;height:165px}
.card .sep{position:absolute;left:10px;top:182px;width:190px;height:1px;background:#e3e3e3}
.card .t{position:absolute;left:0;width:100%;text-align:center}
.card .name{top:202px;font-family:"PT Serif",Georgia,serif;font-weight:700;font-size:14px;color:var(--gold)}
.card .sub{top:221px;font-size:10.5px;color:#555}
.card .stars{top:244px;font-size:14px;letter-spacing:2px;color:var(--star)}
.card .from{top:274px;font-size:10px;color:#666}
.card .price{top:285px;font-family:"PT Serif",Georgia,serif;font-size:26px;color:#333}
.card .per{top:315px;font-size:10px;color:#666}
.card .bar{position:absolute;left:-1px;bottom:-1px;width:212px;height:37px;background:var(--gold);color:var(--white);font-size:11.5px;overflow:hidden}
.card .bar .more{position:absolute;left:10px;top:11px}
.card .bar .cart{position:absolute;left:122px;top:11px;display:flex;align-items:center;gap:5px}
.card .bar::after{content:"";position:absolute;left:98px;top:-4px;width:1.5px;height:46px;background:rgba(255,255,255,.85);transform:rotate(-25deg)}

/* product tones */
.acai{background:radial-gradient(ellipse 35% 48% at 50% 55%,#5a2e1a 0%,#8a5535 55%,rgba(255,255,255,0) 100%)}
.coq-blue{background:radial-gradient(ellipse 32% 48% at 50% 55%,#2f6fb5 0%,#cfe0f0 60%,rgba(255,255,255,0) 100%)}
.coq-green{background:radial-gradient(ellipse 32% 48% at 50% 55%,#7fb33a 0%,#e4efd2 60%,rgba(255,255,255,0) 100%)}
.coq-dark{background:radial-gradient(ellipse 32% 48% at 50% 55%,#1e1e1e 0%,#d8d8d8 60%,rgba(255,255,255,0) 100%)}
.coq-red{background:radial-gradient(ellipse 32% 48% at 50% 55%,#b8323e 0%,#f0d4d4 60%,rgba(255,255,255,0) 100%)}
.coq-purple{background:radial-gradient(ellipse 32% 48% at 50% 55%,#3e1f5c 0%,#ddd0ea 60%,rgba(255,255,255,0) 100%)}
.coq-pink{background:radial-gradient(ellipse 32% 48% at 50% 55%,#1f5a2a 0%,#f6d9ec 60%,rgba(255,255,255,0) 100%)}
.coq-lime{background:radial-gradient(ellipse 32% 48% at 50% 55%,#2a5a1a 0%,#dcefc4 60%,rgba(255,255,255,0) 100%)}
.coq-sky{background:radial-gradient(ellipse 32% 48% at 50% 55%,#1d3a6a 0%,#cfe3f4 60%,rgba(255,255,255,0) 100%)}

/* subscribe */
.subscribe{left:0;top:1605px;width:1200px;height:491px;background:linear-gradient(90deg,#f3f3f3 0%,#eeeeee 40%,#e2ddd8 62%,#d9b9a0 78%,#e9e4df 100%)}
.sub-title{left:95px;top:1668px;font-size:34px;color:#333}
.sub-copy{left:95px;top:1711px;width:470px;font-size:12px;line-height:15px;color:#444}
.field{left:95px;width:391px;height:40px;border:1px solid #c9c9c9;background:rgba(255,255,255,.55);font-size:11px;color:#555;padding:12px 10px}
.field svg{position:absolute;right:9px;top:12px}
.btn-submit{left:95px;top:1943px;width:230px;height:48px;background:var(--gold);color:var(--white);font-family:"PT Serif",Georgia,serif;font-size:19px;letter-spacing:1px;text-align:center;line-height:48px;border-radius:2px}

/* top sellers */
.sellers-title{top:2126px;font-size:30px;font-weight:700;color:#333}
.sellers-rule{left:447px;top:2178px;width:306px;height:1px;background:#c2c2c2}
.sellers-rule::after{content:"";position:absolute;left:123px;top:-1px;width:60px;height:3px;background:var(--gold)}
.rail{top:2200px;width:1px;height:437px;background:linear-gradient(180deg,rgba(0,0,0,0),#cfcfcf 50%,rgba(0,0,0,0))}
.arrow{top:2400px;font-size:30px;color:#333;font-family:"PT Serif",Georgia,serif}
.seller{width:211px;height:388px;border:1px solid #dedede;background:var(--white)}
.seller .thumb{position:absolute;left:10px;top:10px;width:190px;height:175px}
.seller .sep{position:absolute;left:10px;top:192px;width:190px;height:1px;background:#e3e3e3}
.seller .t{position:absolute;left:0;width:100%;text-align:center}
.seller .name{top:203px;font-family:"PT Serif",Georgia,serif;font-weight:700;font-size:14px;color:var(--gold)}
.seller .sub{top:222px;font-size:10.5px;color:#555}
.seller .stars{top:242px;font-size:14px;letter-spacing:2px;color:var(--star)}
.seller .from{top:268px;font-size:10px;color:#666}
.seller .price{top:279px;font-family:"PT Serif",Georgia,serif;font-size:26px;color:#333}
.seller .per{top:309px;font-size:10px;color:#666}
.seller .more{top:326px;font-size:10px;color:#444}
.seller .bar{position:absolute;left:-1px;bottom:-1px;width:211px;height:37px;background:var(--gold);color:var(--white);font-size:11.5px;display:flex;align-items:center;justify-content:center;gap:5px}

/* testimonials / about */
.panel{top:2655px;height:325px;background:linear-gradient(135deg,#2a2521,#14110f 60%,#241e19)}
.panel::before{content:"";position:absolute;left:6px;top:6px;right:6px;bottom:6px;border:1px dashed rgba(255,255,255,.45)}
.panel h2{position:absolute;left:0;top:20px;width:100%;text-align:center;font-family:"PT Serif",Georgia,serif;font-size:24px;color:var(--white)}
.avatar{left:207px;top:63px;width:87px;height:87px;border-radius:50%;border:3px solid var(--white);background:radial-gradient(circle at 50% 40%,#e8c9a5,#b98d5f)}
.quote-name{left:0;top:184px;width:100%;text-align:center;font-family:"PT Serif",Georgia,serif;font-size:13px;color:var(--gold-light)}
.quote{left:35px;top:205px;width:431px;text-align:center;font-size:10.5px;line-height:15px;font-style:italic;color:#eee}
.quote-nav{left:0;top:286px;width:100%;text-align:center;font-size:14px;color:var(--gold-light);letter-spacing:6px}
.about-copy{left:30px;top:78px;width:438px;text-align:center;font-size:12px;line-height:17px;font-style:italic;color:#f0f0f0}
.read-more{left:0;top:277px;width:100%;text-align:center;font-family:"PT Serif",Georgia,serif;font-size:15px;color:var(--gold-light)}

/* footer */
.footer{left:0;top:3023px;width:1200px;height:334px;background:var(--dark)}
.fcol{top:40px}
.fcol h4{font-family:"PT Serif",Georgia,serif;font-weight:400;font-size:14px;color:var(--gold-light);text-transform:uppercase;margin-bottom:10px}
.fcol li{list-style:none;font-size:11px;color:var(--white);line-height:24px}
.fcol li.on{color:var(--gold-light)}
.fcol .lbl{font-family:"PT Serif",Georgia,serif;font-size:12px;color:var(--gold-light);margin-top:6px}
.fcol .num{font-size:13px;color:var(--white);margin-top:6px;margin-bottom:18px}
.news-item{font-size:11px;line-height:15px;color:var(--white);width:270px;margin-bottom:8px}
.news-item b{display:block;font-weight:400;color:var(--gold-light)}
.follow{left:990px;top:27px;width:74px;height:25px;background:var(--gold);color:var(--white);font-size:10.5px;display:flex;align-items:center;gap:5px;padding-left:6px}
.follow i{width:9px;height:9px;background:var(--white)}
.soc{left:997px;width:11px;height:11px;border-radius:50%;background:#e6e6e6}
.payments{left:352px;top:205px;display:flex;gap:14px;align-items:center}
.payments span{height:30px;background:#6d6d6d;border-radius:3px}
.copyright{left:0;top:3357px;width:1200px;height:36px;background:var(--gold);color:#2a2a2a;font-size:11px;text-align:center;line-height:36px}
</style>
</head>
<body>

<!-- top bar -->
<div class="abs topbar">
  <div class="social" aria-label="Social links"><span></span><span></span><span></span><span></span><span></span></div>
  <div class="account"><span>Log In</span><span>Sign Up</span></div>
</div>

<!-- header -->
<div class="abs phone">+44 800 555 0142</div>
<div class="abs brand">
  <div class="brand-mark"></div>
  <div class="brand-name">LUMEN | VALE | WELLNESS</div>
</div>
<div class="abs side-tab">
  <div class="ic" style="top:9px"><svg width="12" height="12" viewBox="0 0 12 12"><path d="M1 6L6 1.5 11 6M2.5 5v5.5h7V5" fill="none" stroke="#fff" stroke-width="1.5"/></svg></div>
  <div class="ic" style="top:53px"><svg width="12" height="12" viewBox="0 0 12 12"><path d="M6 10.5L1.5 6A2.5 2.5 0 016 2.8 2.5 2.5 0 0110.5 6z" fill="#fff"/></svg></div>
  <div class="ic" style="top:98px"><svg width="12" height="12" viewBox="0 0 12 12"><circle cx="5" cy="5" r="3.3" fill="none" stroke="#fff" stroke-width="1.5"/><path d="M7.5 7.5L11 11" stroke="#fff" stroke-width="1.6"/></svg></div>
</div>
<nav class="abs nav">
  <span>HOME</span><span>ABOUT US</span><span>PRODUCT <span class="caret">▾</span></span><span>PRICES</span><span>NEWS</span><span>CONTACT</span>
</nav>
<div class="abs nav-rule"></div>
<ul class="abs dropdown">
  <li>Skin Lightening tablets</li>
  <li>Skin Lightening Creams</li>
  <li>Skin Lightening Soaps</li>
  <li>Skin Lightening Vials</li>
  <li>Skin Lightening Systems</li>
</ul>

<!-- hero -->
<section class="abs hero" role="img" aria-label="Spa scene with a relaxing client and a row of skincare bottles, jars and droppers">
  <div class="abs hero-shade"></div>
  <div class="abs hero-products"></div>
  <div class="abs hero-copy">
    <div class="hello">Welcome to</div>
    <div class="title">LUMEN VALE WELLNESS</div>
    <p>Lorem Ipsum is simply dummy text of the printing and typesetting industry. Lorem Ipsum has been the industry's standard dummy text ever since the 1500s, when an unknown printer took a galley of type</p>
  </div>
  <div class="abs btn-offer">View Offer</div>
  <div class="abs badge-off"><b>20</b><small>%<br>off</small></div>
  <div class="abs dots"><span></span><span></span><span></span></div>
</section>

<!-- shop -->
<h2 class="abs section-title shop-title">SHOP</h2>
<div class="abs shop-rule"></div>
<div class="abs filters"><span class="on">All</span><span>Tablets</span><span>Creams</span><span>Soaps</span><span>Vials</span><span>Systems</span></div>

<!-- row 1 -->
<div class="abs card" style="left:95px;top:784px">
  <div class="thumb acai" role="img" aria-label="Brown supplement bottle"></div><div class="sep"></div>
  <div class="t name">Acai Berry</div><div class="t sub">(4000mg x 180 tablets)</div><div class="t stars">★★★★★</div>
  <div class="t from">from</div><div class="t price">£14.99</div><div class="t per">per bottle</div>
  <div class="bar"><span class="more">More Details</span><span class="cart"><svg width="12" height="11" viewBox="0 0 12 11"><path d="M0 1h2l1.5 6h6.5L11.5 2.5H3" fill="none" stroke="#fff" stroke-width="1.3"/><circle cx="4.5" cy="9.5" r="1" fill="#fff"/><circle cx="9" cy="9.5" r="1" fill="#fff"/></svg>Add to Cart</span></div>
</div>
<div class="abs card" style="left:361px;top:784px">
  <div class="thumb coq-blue" role="img" aria-label="Blue supplement pouch"></div><div class="sep"></div>
  <div class="t name">Coenzyme</div><div class="t sub">(Q10 300mg)</div><div class="t stars">★★★★★</div>
  <div class="t from">from</div><div class="t price">£16.00</div><div class="t per">per bottle</div>
  <div class="bar"><span class="more">More Details</span><span class="cart"><svg width="12" height="11" viewBox="0 0 12 11"><path d="M0 1h2l1.5 6h6.5L11.5 2.5H3" fill="none" stroke="#fff" stroke-width="1.3"/><circle cx="4.5" cy="9.5" r="1" fill="#fff"/><circle cx="9" cy="9.5" r="1" fill="#fff"/></svg>Add to Cart</span></div>
</div>
<div class="abs card" style="left:627px;top:784px">
  <div class="thumb coq-green" role="img" aria-label="Green supplement pouch"></div><div class="sep"></div>
  <div class="t name">Coenzyme</div><div class="t sub">(Q10 300mg)</div><div class="t stars">★★★★★</div>
  <div class="t from">from</div><div class="t price">£20.99</div><div class="t per">per bottle</div>
  <div class="bar"><span class="more">More Details</span><span class="cart"><svg width="12" height="11" viewBox="0 0 12 11"><path d="M0 1h2l1.5 6h6.5L11.5 2.5H3" fill="none" stroke="#fff" stroke-width="1.3"/><circle cx="4.5" cy="9.5" r="1" fill="#fff"/><circle cx="9" cy="9.5" r="1" fill="#fff"/></svg>Add to Cart</span></div>
</div>
<div class="abs card" style="left:893px;top:784px">
  <div class="thumb acai" role="img" aria-label="Brown supplement bottle"></div><div class="sep"></div>
  <div class="t name">Acai Berry</div><div class="t sub">(4000mg x 180 tablets)</div><div class="t stars">★★★★★</div>
  <div class="t from">from</div><div class="t price">£15.99</div><div class="t per">per bottle</div>
  <div class="bar"><span class="more">More Details</span><span class="cart"><svg width="12" height="11" viewBox="0 0 12 11"><path d="M0 1h2l1.5 6h6.5L11.5 2.5H3" fill="none" stroke="#fff" stroke-width="1.3"/><circle cx="4.5" cy="9.5" r="1" fill="#fff"/><circle cx="9" cy="9.5" r="1" fill="#fff"/></svg>Add to Cart</span></div>
</div>

<!-- row 2 -->
<div class="abs card" style="left:95px;top:1191px">
  <div class="thumb acai" role="img" aria-label="Brown supplement bottle"></div><div class="sep"></div>
  <div class="t name">Acai Berry</div><div class="t sub">(4000mg x 180 tablets)</div><div class="t stars">★★★★★</div>
  <div class="t from">from</div><div class="t price">£37.00</div><div class="t per">per bottle</div>
  <div class="bar"><span class="more">More Details</span><span class="cart"><svg width="12" height="11" viewBox="0 0 12 11"><path d="M0 1h2l1.5 6h6.5L11.5 2.5H3" fill="none" stroke="#fff" stroke-width="1.3"/><circle cx="4.5" cy="9.5" r="1" fill="#fff"/><circle cx="9" cy="9.5" r="1" fill="#fff"/></svg>Add to Cart</span></div>
</div>
<div class="abs card" style="left:361px;top:1191px">
  <div class="thumb coq-dark" role="img" aria-label="Black supplement pouch"></div><div class="sep"></div>
  <div class="t name">Coenzyme</div><div class="t sub">(Q10 300mg)</div><div class="t stars">★★★★★</div>
  <div class="t from">from</div><div class="t price">£11.99</div><div class="t per">per bottle</div>
  <div class="bar"><span class="more">More Details</span><span class="cart"><svg width="12" height="11" viewBox="0 0 12 11"><path d="M0 1h2l1.5 6h6.5L11.5 2.5H3" fill="none" stroke="#fff" stroke-width="1.3"/><circle cx="4.5" cy="9.5" r="1" fill="#fff"/><circle cx="9" cy="9.5" r="1" fill="#fff"/></svg>Add to Cart</span></div>
</div>
<div class="abs card" style="left:627px;top:1191px">
  <div class="thumb acai" role="img" aria-label="Brown supplement bottle"></div><div class="sep"></div>
  <div class="t name">Acai Berry</div><div class="t sub">(4000mg x 180 tablets)</div><div class="t stars">★★★★★</div>
  <div class="t from">from</div><div class="t price">£21.00</div><div class="t per">per bottle</div>
  <div class="bar"><span class="more">More Details</span><span class="cart"><svg width="12" height="11" viewBox="0 0 12 11"><path d="M0 1h2l1.5 6h6.5L11.5 2.5H3" fill="none" stroke="#fff" stroke-width="1.3"/><circle cx="4.5" cy="9.5" r="1" fill="#fff"/><circle cx="9" cy="9.5" r="1" fill="#fff"/></svg>Add to Cart</span></div>
</div>
<div class="abs card" style="left:893px;top:1191px">
  <div class="thumb coq-red" role="img" aria-label="Red and white supplement pouch"></div><div class="sep"></div>
  <div class="t name">Acai Berry</div><div class="t sub">(4000mg x 180 tablets)</div><div class="t stars">★★★★★</div>
  <div class="t from">from</div><div class="t price">£15.99</div><div class="t per">per bottle</div>
  <div class="bar"><span class="more">More Details</span><span class="cart"><svg width="12" height="11" viewBox="0 0 12 11"><path d="M0 1h2l1.5 6h6.5L11.5 2.5H3" fill="none" stroke="#fff" stroke-width="1.3"/><circle cx="4.5" cy="9.5" r="1" fill="#fff"/><circle cx="9" cy="9.5" r="1" fill="#fff"/></svg>Add to Cart</span></div>
</div>

<!-- subscribe -->
<section class="abs subscribe" role="img" aria-label="Smiling woman in a white towel talking on the phone in a bright bathroom"></section>
<h2 class="abs serif sub-title" style="font-weight:400">Subscribe Your Email</h2>
<p class="abs sub-copy">Lorem Ipsum is simply dummy text of the printing and typesetting industry. Lorem Ipsum has been the industry's standard dummy text ever since the 1500s, when an unknown print</p>
<div class="abs field" style="top:1796px">Your Name :<svg width="14" height="14" viewBox="0 0 14 14"><circle cx="7" cy="4.5" r="3" fill="#a8803f"/><path d="M1.5 13.5c0-3.5 2.5-5 5.5-5s5.5 1.5 5.5 5z" fill="#a8803f"/></svg></div>
<div class="abs field" style="top:1864px">Your Email :<svg width="15" height="12" viewBox="0 0 15 12"><rect x="0.5" y="1" width="14" height="10" fill="#a8803f"/><path d="M1 1.5l6.5 5 6.5-5" fill="none" stroke="#fff" stroke-width="1"/></svg></div>
<div class="abs btn-submit">SUBMIT</div>

<!-- top sellers -->
<h2 class="abs section-title sellers-title">Top Sellers</h2>
<div class="abs sellers-rule"></div>
<div class="abs rail" style="left:141px"></div>
<div class="abs rail" style="left:1061px"></div>
<div class="abs arrow" style="left:108px">‹</div>
<div class="abs arrow" style="left:1078px">›</div>

<div class="abs seller" style="left:152px;top:2221px">
  <div class="thumb coq-purple" role="img" aria-label="Purple supplement pouch"></div><div class="sep"></div>
  <div class="t name">Coenzyme</div><div class="t sub">(Q10 300mg)</div><div class="t stars">★★★★★</div>
  <div class="t from">from</div><div class="t price">£11.99</div><div class="t per">per bottle</div><div class="t more">More Details</div>
  <div class="bar"><svg width="12" height="11" viewBox="0 0 12 11"><path d="M0 1h2l1.5 6h6.5L11.5 2.5H3" fill="none" stroke="#fff" stroke-width="1.3"/><circle cx="4.5" cy="9.5" r="1" fill="#fff"/><circle cx="9" cy="9.5" r="1" fill="#fff"/></svg>Add to Cart</div>
</div>
<div class="abs seller" style="left:380px;top:2221px">
  <div class="thumb coq-pink" role="img" aria-label="Pink supplement pouch"></div><div class="sep"></div>
  <div class="t name">Coenzyme</div><div class="t sub">(Q10 300mg)</div><div class="t stars">★★★★★</div>
  <div class="t from">from</div><div class="t price">£11.99</div><div class="t per">per bottle</div><div class="t more">More Details</div>
  <div class="bar"><svg width="12" height="11" viewBox="0 0 12 11"><path d="M0 1h2l1.5 6h6.5L11.5 2.5H3" fill="none" stroke="#fff" stroke-width="1.3"/><circle cx="4.5" cy="9.5" r="1" fill="#fff"/><circle cx="9" cy="9.5" r="1" fill="#fff"/></svg>Add to Cart</div>
</div>
<div class="abs seller" style="left:609px;top:2221px">
  <div class="thumb coq-lime" role="img" aria-label="Lime green supplement pouch"></div><div class="sep"></div>
  <div class="t name">Coenzyme</div><div class="t sub">(Q10 300mg)</div><div class="t stars">★★★★★</div>
  <div class="t from">from</div><div class="t price">£11.99</div><div class="t per">per bottle</div><div class="t more">More Details</div>
  <div class="bar"><svg width="12" height="11" viewBox="0 0 12 11"><path d="M0 1h2l1.5 6h6.5L11.5 2.5H3" fill="none" stroke="#fff" stroke-width="1.3"/><circle cx="4.5" cy="9.5" r="1" fill="#fff"/><circle cx="9" cy="9.5" r="1" fill="#fff"/></svg>Add to Cart</div>
</div>
<div class="abs seller" style="left:836px;top:2221px">
  <div class="thumb coq-sky" role="img" aria-label="Light blue supplement pouch"></div><div class="sep"></div>
  <div class="t name">Coenzyme</div><div class="t sub">(Q10 300mg)</div><div class="t stars">★★★★★</div>
  <div class="t from">from</div><div class="t price">£11.99</div><div class="t per">per bottle</div><div class="t more">More Details</div>
  <div class="bar"><svg width="12" height="11" viewBox="0 0 12 11"><path d="M0 1h2l1.5 6h6.5L11.5 2.5H3" fill="none" stroke="#fff" stroke-width="1.3"/><circle cx="4.5" cy="9.5" r="1" fill="#fff"/><circle cx="9" cy="9.5" r="1" fill="#fff"/></svg>Add to Cart</div>
</div>

<!-- testimonials -->
<section class="abs panel" style="left:95px;width:501px" role="img" aria-label="Dark, softly lit portrait backdrop">
  <h2>Testimonials</h2>
  <div class="abs avatar" role="img" aria-label="Customer portrait"></div>
  <div class="abs quote-name">Rosalind</div>
  <p class="abs quote">Lorem Ipsum is simply dummy text of the printing and typesetting industry. Lorem Ipsum has been the industry's standard dummy text ever since the 1500s, when an unknown printer took a galley of typeLorem Ipsum is simply dummy text of the printing and typesetting industry. Lorem Ipsum has been the industry's standard dummy text ever since the 1500s, when an unknown printer took a galley of type</p>
  <div class="abs quote-nav">‹ ›</div>
</section>

<!-- about -->
<section class="abs panel" style="left:607px;width:498px">
  <h2>About Us</h2>
  <p class="abs about-copy">Lorem Ipsum is simply dummy text of the printing and typesetting industry. Lorem Ipsum has been the industry's standard dummy text ever since the 1500s, when an unknown printer took a galley of type and scrambled it to make a type specimen book. It has survived not only five centuries, but also the leap into electronic typesetting, remaining essentially unchanged. It was popularised in the 1960s with the release of Letraset sheets containing Lorem Ipsum passages, and more recently with desktop publishing software like Aldus PageMaker including versions of Lorem Ipsum Lorem Ipsum is simply dummy text of the printing and typesetting industry. Lorem Ipsum has been the industry's standard dummy text ever since the</p>
  <div class="abs read-more">READ MORE</div>
</section>

<!-- footer -->
<footer class="abs footer">
  <div class="abs fcol" style="left:95px">
    <h4>Site Map</h4>
    <ul><li class="on">› Home</li><li>› About Us</li><li>› Product</li><li>› Prices</li><li>› News</li><li>› Contact</li></ul>
  </div>
  <div class="abs fcol" style="left:245px">
    <h4>Quick Links</h4>
    <ul><li>› About Us</li><li>› Contact Us</li><li>› Delivery Info</li><li>› Customer Testimonials</li><li>› Read our Revura reviews</li><li>› Read our Starvox reviews</li></ul>
  </div>
  <div class="abs fcol" style="left:450px">
    <h4>Contact</h4>
    <div class="lbl">Calling from the UK</div>
    <div class="num">0800 555 0142</div>
    <div class="lbl">Calling from Overseas</div>
    <div class="num">+44 800 555 0142</div>
  </div>
  <div class="abs fcol" style="left:645px">
    <h4>News</h4>
    <div class="news-item" style="margin-top:18px"><b>Lorem Ipsum is simply dummy</b>Lorem Ipsum is simply dummy text of the printing and typesetting industry. Lorem</div>
    <div class="news-item"><b>Lorem Ipsum is simply dummy</b>Lorem Ipsum is simply dummy text of the printing and typesetting industry. Lorem</div>
  </div>
  <div class="abs fcol" style="left:1010px"><h4>Social Media</h4></div>
  <div class="abs follow"><i></i>Follow us</div>
  <span class="abs soc" style="top:84px"></span>
  <span class="abs soc" style="top:115px"></span>
  <span class="abs soc" style="top:146px"></span>
  <span class="abs soc" style="top:177px"></span>
  <div class="abs payments" aria-label="Accepted payment methods">
    <span style="width:50px;opacity:.5"></span><span style="width:46px;opacity:.5"></span>
    <span style="width:44px;border-radius:15px"></span><span style="width:44px;border-radius:15px"></span>
    <span style="width:6px;background:none"></span>
    <span style="width:52px"></span><span style="width:56px"></span><span style="width:52px"></span><span style="width:26px"></span>
  </div>
</footer>
<div class="abs copyright">© 2016 | All Rights Reserved</div>

</body>
</html>
```